An Agro-Processor Needs Packaging Design for Line-Extensions & New Variants

We are a producer of Frondique dried tropical fruits (www.kelvoruna.com) based in Uganda. We have our base variants of dried mango, dried pineapple, dried banana, dried papaya and dried jackfruit on shelf and now need to develop packaging designs (stand-up zipper pouches) for line-extensions at premium price points while maintaining a strong family look with the existing base variants. The line-extensions include:

- Roasted & Salted Nuts (part of the base range)
- Coated Nuts (new premium range)
- Coated Dried Fruits (new premium range)
- Salad/Breakfast Toppings (new premium range)

Attachments:
- Find attached packaging copy for the entire range
- Please see attached notes about the color/design recommendations for each of the range above
- Find attached images for some competitor products for inspiration (intention is to get inspiration not to infringe on their design)
- Find attached design file for the base variant. The name of the font used is Gooddog Cool
- Find attached design file for the 'frondique' brand name
- Find attached a beauty shot of the complete base range
- Find attached beauty product shots (it is NOT mandatory to use these, you are free to use whatever you want). The attached images are proprietary, it is prohibited to use the image for any other purposed than for the purpose of this brief

Target Market(s)

Organic and natural living enthusiasts who would pay a premium to get the best for them and their families

Colors

Designer to choose colors to be used in the design.

Requirements
Must have
• - Strong family look with the existing base variants, HOWEVER establish adequate differentiation between the ranges
• - Maintain an overall white look for the fruit range, develop an overall 'natural' brown look for the nuts range and develop an overall black/edgy look for salad/breakfast mixes
• - As much as possible, maintain the positioning of the brand name on pack so that when merchandised side by side, it creates a big brand impact
• - Please always include an image of the base variant in all your submissions for comparison

```html
<!DOCTYPE html>
<html lang="en">
<head>
<meta charset="UTF-8">
<title>Frondique Pouch Range</title>
<link href="https://fonts.googleapis.com/css2?family=Caveat+Brush&family=Tinos:wght@400;700&family=Open+Sans:wght@600&display=swap" rel="stylesheet">
<style>
  :root {
    --canvas-bg: #eef1f0;
    --fruit-yellow: #e0b81c;
    --fruit-white: #f3f3f3;
    --mix-green: #6ab12f;
    --mix-black: #2a2728;
    --nut-brown: #a8742e;
    --nut-gold: #d9b56a;
    --nut-cream: #f2e7cf;
    --ink-brown: #5a2a1c;
    --ink-grey: #6b6b6b;
    --sun-orange: #f0a81c;
    --white: #ffffff;
  }
  * { margin: 0; padding: 0; box-sizing: border-box; }
  html, body { width: 1200px; height: 771px; overflow: hidden; }
  body { background: var(--canvas-bg); position: relative; font-family: "Tinos", serif; }

  .pouch {
    position: absolute; top: 140px; width: 300px; height: 490px;
    border-radius: 6px 6px 4px 4px; overflow: hidden;
    box-shadow: 0 14px 30px rgba(0,0,0,.15);
  }
  .pouch--fruit { left: 120px; background: linear-gradient(180deg, #fafafa, var(--fruit-white)); }
  .pouch--mix   { left: 450px; background: var(--mix-black); }
  .pouch--nuts  { left: 780px; background: linear-gradient(180deg, var(--nut-gold), var(--nut-cream) 70%); }

  .brand-panel {
    position: absolute; left: 36px; right: 36px; top: 0; height: 180px;
    display: flex; align-items: flex-end; justify-content: center; padding-bottom: 26px;
  }
  .pouch--fruit .brand-panel { background: var(--fruit-yellow); }
  .pouch--mix .brand-panel { background: var(--mix-green); left: 20px; right: 60px; }
  .pouch--nuts .brand-panel { background: var(--nut-brown); }
  .brand-name { font-family: "Tinos", serif; font-size: 34px; color: var(--ink-brown); }
  .pouch--nuts .brand-name { color: #4a2314; }

  .sun {
    position: absolute; width: 96px; height: 96px; border-radius: 50%;
    background: radial-gradient(circle, var(--sun-orange) 55%, rgba(240,168,28,.35) 56%, rgba(240,168,28,0) 72%);
  }
  .pouch--fruit .sun { right: 22px; top: 218px; }
  .pouch--mix .sun { right: 8px; top: 110px; }
  .pouch--nuts .sun { right: 18px; top: 232px; }

  .product-title {
    position: absolute; left: 0; right: 0; text-align: center;
    font-family: "Caveat Brush", cursive; color: var(--ink-brown); line-height: .95;
  }
  .pouch--fruit .product-title { top: 200px; font-size: 44px; }
  .pouch--mix .product-title { top: 180px; font-size: 60px; color: var(--white); }
  .pouch--nuts .product-title { top: 200px; font-size: 44px; }
  .product-subtitle { display: block; font-family: "Tinos", serif; font-size: 16px; color: var(--mix-green); margin-top: 2px; }

  .product-photo { position: absolute; left: 50%; transform: translateX(-50%); }
  .pouch--fruit .product-photo { top: 300px; width: 170px; height: 110px; border-radius: 50%; background: radial-gradient(circle, #f2b51c, #d88f12 70%, rgba(216,143,18,0) 72%); }
  .pouch--mix .product-photo { top: 272px; width: 130px; height: 130px; border-radius: 50%; background: radial-gradient(circle, #7a5a30 0%, #4f7a2e 55%, #f4f1ea 66%); box-shadow: 0 4px 10px rgba(0,0,0,.3); z-index: 2; }
  .pouch--nuts .product-photo { top: 300px; width: 190px; height: 110px; border-radius: 50%; background: radial-gradient(circle, #e2b85a, #c89a3e 68%, rgba(200,154,62,0) 72%); }

  .mix-base {
    position: absolute; left: -40px; right: -40px; bottom: 0; height: 190px;
    background: var(--white); border-top: 6px solid var(--mix-green);
    border-radius: 60% 60% 0 0 / 40% 40% 0 0;
  }

  .claims {
    position: absolute; left: 0; right: 0; bottom: 48px; text-align: center;
    font-size: 13px; color: var(--ink-grey); line-height: 1.25;
  }
  .claims .origin { font-weight: 700; color: var(--ink-brown); font-size: 14px; }
  .net-weight {
    position: absolute; right: 22px; bottom: 14px; text-align: right;
    font-family: "Open Sans", sans-serif; font-size: 9px; color: #444;
  }
  .net-weight strong { display: block; font-size: 13px; font-weight: 600; letter-spacing: 1px; }
  .badge { position: absolute; left: 16px; bottom: 16px; width: 30px; height: 32px; border-radius: 4px; }
  .pouch--fruit .badge { background: var(--fruit-yellow); }
  .pouch--mix .badge { background: var(--mix-green); }
  .pouch--nuts .badge { background: #7a3a22; }
</style>
</head>
<body>
  <section class="pouch pouch--fruit">
    <div class="brand-panel"><span class="brand-name">frondique</span></div>
    <div class="sun" role="img" aria-label="Sun motif"></div>
    <h2 class="product-title">Chia<br>Pineapple</h2>
    <div class="product-photo" role="img" aria-label="Photo of dried pineapple pieces with chia seeds"></div>
    <p class="claims">Contains Nothing Artificial<br><span class="origin">Ugandan Origin</span></p>
    <div class="badge"></div>
    <p class="net-weight">Net Weight<strong>100g</strong></p>
  </section>

  <section class="pouch pouch--mix">
    <div class="brand-panel"><span class="brand-name">frondique</span></div>
    <div class="sun" role="img" aria-label="Sun motif"></div>
    <h2 class="product-title">Mixes<span class="product-subtitle">Hawaiian Salad</span></h2>
    <div class="mix-base"></div>
    <div class="product-photo" role="img" aria-label="Photo of a bowl of Hawaiian salad with fruit and nuts"></div>
    <p class="claims">Contains Nothing Artificial<br><span class="origin">Ugandan Origin</span></p>
    <div class="badge"></div>
    <p class="net-weight">Net Weight<strong>100g</strong></p>
  </section>

  <section class="pouch pouch--nuts">
    <div class="brand-panel"><span class="brand-name">frondique</span></div>
    <div class="sun" role="img" aria-label="Sun motif"></div>
    <h2 class="product-title">Roasted &amp;<br>Salted Nuts</h2>
    <div class="product-photo" role="img" aria-label="Photo of roasted salted cashews with seeds"></div>
    <p class="claims">Contains Nothing Artificial<br><span class="origin">Ugandan Origin</span></p>
    <div class="badge"></div>
    <p class="net-weight">Net Weight<strong>100g</strong></p>
  </section>
</body>
</html>
```